New Webpage for High Class Expert Witness Services Company

We are looking for a minimalist design for a webpage that just has our logo and an entry form offer to connect with one of our Liaisons.
The entry form should just ask for Name, Email, Contact Info and Description of Project.

Company Name is: The Marlow Crest Advisory Services

Number of Pages Required

1 page

```html
<!DOCTYPE html>
<html lang="en">
<head>
<meta charset="utf-8">
<title>The Marlow Crest Advisory Services – Connect Now</title>
<link rel="stylesheet" href="https://fonts.googleapis.com/css2?family=Cinzel:wght@400;600&family=Poppins:wght@400;500;600;700&display=swap">
<style>
  :root {
    --charcoal: #2e2e2e;
    --copper: #b07247;
    --blush: #fcf3f1;
    --white: #ffffff;
    --ink: #1e1e1e;
    --rule: #d9d2cf;
  }
  * { box-sizing: border-box; margin: 0; padding: 0; }
  html, body { width: 978px; height: 1200px; overflow: hidden; }
  body { position: relative; background: var(--blush); font-family: "Poppins", sans-serif; color: var(--ink); }

  .site-header { position: absolute; left: 0; top: 0; width: 978px; height: 92px; background: var(--charcoal); }
  .brand { position: absolute; left: 91px; top: 30px; color: #e6e6e6; font-family: "Cinzel", serif; font-weight: 400; font-size: 17px; line-height: 1.15; letter-spacing: 0.5px; }
  .brand small { display: block; font-size: 17px; }
  .header-phone { position: absolute; left: 628px; top: 28px; display: flex; align-items: center; gap: 14px; color: var(--white); font-weight: 600; font-size: 15.4px; }
  .phone-badge { width: 36px; height: 36px; border-radius: 50%; background: var(--copper); display: flex; align-items: center; justify-content: center; }

  .hero { position: absolute; left: 0; top: 92px; width: 978px; height: 454px; background: linear-gradient(100deg, #d6d6d6 0%, #a9a9a9 30%, #6f6f6f 55%, #8c8c8c 75%, #2f2f2f 100%); }
  .hero-title { position: absolute; left: 0; top: 172px; width: 978px; text-align: center; color: var(--white); font-family: "Cinzel", serif; font-weight: 600; font-size: 42px; line-height: 51px; letter-spacing: 0.5px; text-shadow: 0 2px 8px rgba(0,0,0,0.25); }

  .connect { position: absolute; left: 0; top: 546px; width: 978px; height: 600px; }
  .connect-mark { position: absolute; left: 476px; top: 76px; width: 26px; height: 26px; background: var(--charcoal); }
  .connect-title { position: absolute; left: 0; top: 132px; width: 978px; text-align: center; font-family: "Cinzel", serif; font-weight: 600; font-size: 38px; color: var(--charcoal); letter-spacing: 0.5px; }
  .connect-rule { position: absolute; left: 453px; top: 182px; width: 72px; height: 2px; background: var(--copper); }
  .connect-lead { position: absolute; left: 120px; top: 206px; width: 738px; text-align: center; font-size: 14.7px; line-height: 23px; }
  .connect-lead p + p { margin-top: 12px; }

  .field { position: absolute; background: var(--white); border-radius: 21px; box-shadow: 0 3px 10px rgba(120,90,80,0.12); display: flex; align-items: center; font-size: 12.6px; color: #2a2a2a; }
  .field .icon { width: 44px; height: 30px; display: flex; align-items: center; justify-content: center; border-right: 1px solid var(--rule); }
  .field .label { padding-left: 12px; }
  .field-name { left: 148px; top: 317px; width: 333px; height: 42px; }
  .field-email { left: 148px; top: 371px; width: 333px; height: 42px; }
  .field-phone { left: 148px; top: 424px; width: 333px; height: 42px; }
  .field-project { left: 494px; top: 317px; width: 336px; height: 148px; border-radius: 16px; align-items: flex-start; padding-top: 7px; }
  .field-project .label { padding-top: 7px; }

  .submit { position: absolute; left: 386px; top: 483px; width: 207px; height: 41px; background: var(--copper); color: var(--white); font-weight: 700; font-size: 13.5px; display: flex; align-items: center; justify-content: center; letter-spacing: 0.2px; }

  .site-footer { position: absolute; left: 0; top: 1146px; width: 978px; height: 54px; background: var(--charcoal); color: #ececec; font-size: 11.6px; display: flex; align-items: center; justify-content: center; }
</style>
</head>
<body>
  <header class="site-header">
    <div class="brand">The Marlow Crest<small>Advisory Services</small></div>
    <div class="header-phone">
      <span class="phone-badge">
        <svg width="16" height="16" viewBox="0 0 24 24" fill="#fff"><path d="M6.6 10.8a15.1 15.1 0 0 0 6.6 6.6l2.2-2.2c.3-.3.7-.4 1-.2 1.1.4 2.3.6 3.6.6.6 0 1 .4 1 1V20c0 .6-.4 1-1 1A17 17 0 0 1 3 4c0-.6.4-1 1-1h3.5c.6 0 1 .4 1 1 0 1.3.2 2.5.6 3.6.1.3 0 .7-.2 1z"/></svg>
      </span>
      Call toll free (800) 555-0142
    </div>
  </header>

  <section class="hero" role="img" aria-label="Black and white photo of a doctor in a white coat shaking hands with a businessman in a suit">
    <h1 class="hero-title">SPEAK WITH A DEFENSE<br>LIAISONS TODAY</h1>
  </section>

  <section class="connect">
    <div class="connect-mark"></div>
    <h2 class="connect-title">CONNECT NOW</h2>
    <div class="connect-rule"></div>
    <div class="connect-lead">
      <p>Direct access to experienced professionals for your mission-critical projects.</p>
      <p>Share a few details about your project, and a member of our team will reach out to discuss how we can support your objectives.</p>
    </div>

    <div class="field field-name">
      <span class="icon"><svg width="10" height="11" viewBox="0 0 10 11" fill="#b07247"><circle cx="5" cy="3" r="2.7"/><path d="M0 11c0-3 2-4.6 5-4.6S10 8 10 11z"/></svg></span>
      <span class="label">Your Name</span>
    </div>
    <div class="field field-email">
      <span class="icon"><svg width="13" height="10" viewBox="0 0 13 10" fill="#b07247"><rect width="13" height="10" rx="1"/><path d="M0 1l6.5 4.5L13 1" stroke="#fff" stroke-width="1.2" fill="none"/></svg></span>
      <span class="label">Email</span>
    </div>
    <div class="field field-phone">
      <span class="icon"><svg width="11" height="11" viewBox="0 0 24 24" fill="#b07247"><path d="M6.6 10.8a15.1 15.1 0 0 0 6.6 6.6l2.2-2.2c.3-.3.7-.4 1-.2 1.1.4 2.3.6 3.6.6.6 0 1 .4 1 1V20c0 .6-.4 1-1 1A17 17 0 0 1 3 4c0-.6.4-1 1-1h3.5c.6 0 1 .4 1 1 0 1.3.2 2.5.6 3.6.1.3 0 .7-.2 1z"/></svg></span>
      <span class="label">Phone</span>
    </div>
    <div class="field field-project">
      <span class="icon"><svg width="13" height="11" viewBox="0 0 13 11" fill="#b07247"><ellipse cx="5" cy="4" rx="5" ry="3.6"/><ellipse cx="8.5" cy="6.5" rx="4.5" ry="3.2" opacity="0.8"/></svg></span>
      <span class="label">Project Description</span>
    </div>

    <div class="submit">SUBMIT REQUEST</div>
  </section>

  <footer class="site-footer">Copyright © 2026 The Marlow Crest Advisory Services&nbsp;&nbsp;|&nbsp;&nbsp;All Rights Reserved</footer>
</body>
</html>
```